Flyer overhaul from current flyers

I need to have our current flyers updated with a fresher look. We also need to have a new utility and real estate flyer created that will go along with the design of the new flyer. We are looking for new pictures, new overall design, same color scheme but would like to have the flyers more airy and inviting.

Target Market(s)

decision makers in the healthcare/utilty/banking/real estate sectors

Font styles to use
Other font styles liked:
• Logo is in Bell MT

Colors
0054AA
0677BA
7BADD7
CADEEF
E8F1F8

Requirements
Must have
• Close to what is currently on the existing flyers

```html
<!DOCTYPE html>
<html lang="en">
<head>
<meta charset="utf-8">
<title>Riverbend Recovery – Our Philosophy</title>
<link href="https://fonts.googleapis.com/css2?family=Merriweather:wght@400;700;900&display=swap" rel="stylesheet">
<style>
  :root {
    --royal: #0054aa;
    --ocean: #0677ba;
    --deep: #0b5a8a;
    --sky: #7badd7;
    --mist: #cadeef;
    --frost: #e8f1f8;
    --white: #ffffff;
    --ink: #0e4f7c;
  }
  * { margin: 0; padding: 0; box-sizing: border-box; }
  html, body { width: 925px; height: 1200px; overflow: hidden; background: var(--white); }
  .flyer {
    position: relative;
    width: 925px;
    height: 1200px;
    overflow: hidden;
    background: linear-gradient(180deg, var(--white) 0%, var(--white) 55%, var(--frost) 100%);
    font-family: "Merriweather", Georgia, serif;
  }
  .backdrop { position: absolute; inset: 0; }

  .portrait {
    position: absolute;
    left: 0;
    top: 140px;
    width: 480px;
    height: 1000px;
    border-radius: 0 260px 0 0;
    background:
      radial-gradient(ellipse 150px 190px at 265px 200px, rgba(222, 190, 170, 0.95) 0%, rgba(222, 190, 170, 0) 100%),
      radial-gradient(ellipse 330px 420px at 200px 640px, rgba(255, 255, 255, 0.95) 0%, rgba(255, 255, 255, 0) 100%),
      linear-gradient(180deg, rgba(202, 222, 239, 0.85) 0%, rgba(232, 241, 248, 0.9) 55%, rgba(255, 255, 255, 0) 100%);
    -webkit-mask-image: linear-gradient(180deg, #000 0%, #000 75%, transparent 100%);
            mask-image: linear-gradient(180deg, #000 0%, #000 75%, transparent 100%);
  }

  .brand {
    position: absolute;
    left: 565px;
    top: 52px;
    width: 302px;
    height: 104px;
    border-radius: 20px;
    background: var(--deep);
    display: flex;
    align-items: center;
    gap: 16px;
    padding: 0 22px;
  }
  .brand-dot {
    width: 46px; height: 46px;
    border-radius: 50%;
    background: var(--white);
    flex: none;
  }
  .brand-name {
    color: var(--white);
    font-weight: 400;
    font-size: 25px;
    line-height: 1.1;
    letter-spacing: 0.5px;
  }
  .brand-name span { display: block; }

  .philosophy {
    position: absolute;
    left: 71px;
    top: 577px;
    width: 790px;
    height: 472px;
    border-radius: 28px;
    background: linear-gradient(135deg, rgba(6, 119, 186, 0.93) 0%, rgba(11, 96, 146, 0.95) 60%, rgba(9, 84, 130, 0.97) 100%);
    box-shadow: 0 18px 40px rgba(0, 84, 170, 0.15);
    color: var(--white);
    text-align: center;
    padding: 30px 52px 0;
  }
  .philosophy-title {
    font-weight: 700;
    font-size: 68px;
    line-height: 1.1;
    letter-spacing: 1px;
  }
  .philosophy-rule {
    width: 538px;
    height: 2px;
    margin: 14px auto 22px;
    background: var(--sky);
  }
  .philosophy-body {
    font-size: 20px;
    line-height: 32px;
    font-weight: 400;
    hyphens: auto;
    -webkit-hyphens: auto;
  }

  .call-bar {
    position: absolute;
    left: 71px;
    top: 1087px;
    width: 790px;
    height: 42px;
    border-radius: 21px;
    background: var(--white);
    box-shadow: 0 2px 10px rgba(0, 84, 170, 0.12);
    color: var(--ink);
    font-weight: 700;
    font-size: 30px;
    line-height: 42px;
    text-align: center;
  }
  .web-bar {
    position: absolute;
    left: 203px;
    top: 1157px;
    width: 548px;
    height: 40px;
    border-radius: 6px;
    background: var(--deep);
    color: var(--white);
    font-weight: 700;
    font-size: 18px;
    line-height: 40px;
    text-align: center;
  }
</style>
</head>
<body>
<main class="flyer">
  <svg class="backdrop" width="925" height="1200" viewBox="0 0 925 1200" aria-hidden="true">
    <defs>
      <radialGradient id="glow" cx="0.5" cy="0.5" r="0.5">
        <stop offset="0" stop-color="#ffffff" stop-opacity="0.85"/>
        <stop offset="0.5" stop-color="#cadeef" stop-opacity="0.5"/>
        <stop offset="1" stop-color="#e8f1f8" stop-opacity="0"/>
      </radialGradient>
      <radialGradient id="soft-glow" cx="0.5" cy="0.5" r="0.5">
        <stop offset="0" stop-color="#7badd7" stop-opacity="0.45"/>
        <stop offset="1" stop-color="#e8f1f8" stop-opacity="0"/>
      </radialGradient>
      <linearGradient id="wide-band" x1="0" y1="0" x2="1" y2="1">
        <stop offset="0" stop-color="#0b5a8a"/>
        <stop offset="0.6" stop-color="#0677ba"/>
        <stop offset="1" stop-color="#7badd7"/>
      </linearGradient>
      <linearGradient id="band-fade" x1="0" y1="0" x2="0" y2="1">
        <stop offset="0" stop-color="#ffffff" stop-opacity="1"/>
        <stop offset="0.75" stop-color="#ffffff" stop-opacity="1"/>
        <stop offset="1" stop-color="#ffffff" stop-opacity="0"/>
      </linearGradient>
      <mask id="fade-down">
        <rect width="925" height="620" fill="url(#band-fade)"/>
      </mask>
    </defs>
    <polygon points="334,0 498,0 260,560 150,560" fill="#0b5a8a"/>
    <g mask="url(#fade-down)">
      <polygon points="516,0 925,0 925,600 360,600" fill="url(#wide-band)"/>
      <polygon points="640,0 700,0 520,600 470,600" fill="#ffffff" opacity="0.08"/>
    </g>
    <ellipse cx="640" cy="420" rx="260" ry="200" fill="url(#glow)"/>
    <ellipse cx="880" cy="1080" rx="210" ry="130" fill="url(#soft-glow)"/>
  </svg>

  <div class="portrait" role="img" aria-label="Smiling doctor in a white coat with a stethoscope, arms crossed"></div>

  <div class="brand">
    <span class="brand-dot"></span>
    <div class="brand-name"><span>RIVERBEND</span><span>RECOVERY</span></div>
  </div>

  <section class="philosophy">
    <h1 class="philosophy-title">Our Philosophy</h1>
    <div class="philosophy-rule"></div>
    <p class="philosophy-body">Since our inception, and for over 40 years, healthcare collections have been at the center of our operation. Our philosophy is to provide consistent performance by investing in our clients accounts to ensure the maximum liquidation. By building on historically proven collection techniques and employing an ever-expanding access to data and technology, our agency has continued to improve our performance to the benefit of our clients. Our capital forward, compliance centered approach has proven to deliver consistent results to our healthcare providers.</p>
  </section>

  <div class="call-bar">CALL US AT: (555) 013-4820</div>
  <div class="web-bar">www.riverbendrecovery.com</div>
</main>
</body>
</html>
```